Coming Soon..... Product launch card

Velour Cuisine is a start up company specializing in Executive Aviation Catering Solutions. In short we provide, food, flowers, laundry services, dishwashing and personal shopping assistance to VIP travellers on private jets.

We will launch our business in May 2014, but want to prepare the market for our arrival.

The card should show our logo (which is attached and available in high res) should be predominantly black and gold in colour and only have simple high quality photographs of food, flowers, luxury goods, and/or private jets. Please don't over complicate the card - it should be elegant and simple.

Text on the card should read; (or similar)

Velour Cuisine, (Logo) Executive Aviation Catering
Coming soon to Sefrani Crest International Airport
Contact us for more information, info@velourcuisine.com
Updates

Hi Designers

Further to my brief posted yesterday, I would like to add that I am open to ideas about the size of the card, but was thinking that A6 size would be about right for what we need.

Thanks,

Moira

Hi everyone. 

Please refer back to the brief which I have updated with examples of the kind of images that I prefer.

Thanks

Target Market(s)

Our target audience is the aviation industry - pilots, cabin crew and professionals

Industry/Entity Type

Shopping

Font styles to use
Other font styles liked:
• Josefin San

Requirements
Must have
• Our logo. (Text is Josefin Sans)
Nice to have
• Focus on simple, fresh, colourful photos that evoke feelings of luxury, health great food
Should not have
• Too many images.

```html
<!DOCTYPE html>
<html lang="en">
<head>
<meta charset="utf-8">
<title>Velour Cuisine — Coming Soon Card</title>
<link rel="stylesheet" href="https://fonts.googleapis.com/css2?family=Josefin+Sans:wght@400&family=Open+Sans:wght@700&display=swap">
<style>
  :root {
    --backdrop: #2a2a2a;
    --card-black: #050505;
    --gold-light: #e9c27a;
    --gold-mid: #c9a052;
    --gold-deep: #8c6a2a;
    --gold-text: #c9a050;
    --brand-ink: #7a5a22;
    --photo-plated: #b8906a;
    --photo-chilled: #c8c8c0;
  }
  html, body {
    margin: 0;
    width: 1200px;
    height: 900px;
    overflow: hidden;
    background: var(--backdrop);
  }
  .canvas {
    width: 1200px;
    height: 900px;
    display: flex;
    align-items: center;
    justify-content: center;
  }
  .card {
    width: 450px;
    height: 640px;
    background: var(--card-black);
    padding: 12px;
    box-sizing: border-box;
    display: flex;
    flex-direction: column;
    box-shadow: 0 20px 50px rgba(0,0,0,0.6);
  }
  .photo-row {
    display: flex;
    gap: 8px;
    height: 190px;
  }
  .photo {
    flex: 1;
  }
  .photo--plated {
    background: linear-gradient(160deg, #e8e0d4 0%, var(--photo-plated) 55%, #6e3a2a 100%);
  }
  .photo--chilled {
    background: linear-gradient(180deg, #9a9a94 0%, var(--photo-chilled) 50%, #a8683a 100%);
  }
  .brand-panel {
    margin: 10px -12px 0;
    height: 240px;
    background: radial-gradient(ellipse at 30% 25%, var(--gold-light) 0%, var(--gold-mid) 50%, var(--gold-deep) 100%);
    display: flex;
    align-items: center;
    justify-content: center;
  }
  .brand-name {
    font-family: "Josefin Sans", sans-serif;
    font-weight: 400;
    font-size: 46px;
    letter-spacing: 2px;
    color: var(--brand-ink);
    text-transform: uppercase;
    margin: 0;
  }
  .announcement {
    flex: 1;
    display: flex;
    flex-direction: column;
    align-items: center;
    justify-content: center;
    text-align: center;
    font-family: "Open Sans", sans-serif;
    font-weight: 700;
    color: var(--gold-text);
  }
  .headline {
    margin: 0;
    font-size: 21px;
    line-height: 1.25;
  }
  .contact {
    margin: 24px 0 0;
    font-size: 11px;
  }
</style>
</head>
<body>
  <main class="canvas">
    <article class="card">
      <div class="photo-row">
        <div class="photo photo--plated" role="img" aria-label="Photograph of plated rack of lamb with gratin while sauce is poured"></div>
        <div class="photo photo--chilled" role="img" aria-label="Photograph of sashimi and flowers presented on an ice block before a waterfall"></div>
      </div>
      <div class="brand-panel">
        <h1 class="brand-name">Velour Cuisine</h1>
      </div>
      <section class="announcement">
        <p class="headline">Executive Aviation Catering<br>Coming soon to<br>Sefrani Crest International Airport</p>
        <p class="contact">Contact us for more information, info@velourcuisine.com</p>
      </section>
    </article>
  </main>
</body>
</html>
```